KLV [Kindly Living Ventures]

We require a web design for a new line of products that we have created. The first of these is a product called B-GONE which is a natural product designed to repel animals such as Possums, snakes and Kangaroos in Australia and things like deer and Raccoons in the US.
Our Company and head office are in Sydney Australia and we have our own factories in Taiwan and China.
These items come in a few different forms such as Discs that can be thrown into a roof cavity, to a gell that comes in a PET container for use in the garden around plants and vegetables and an oil based spray that can be used on trucks of trees or plants and fences etc.
The final design should communicate an environmental and safe feeling for the user and also the animals it repels, but also make the user feel safe that they have B-goned the animals that were being a nuisance.

Target Market(s)

Home owners, gardeners, farmers

Industry/Entity Type

It Company

Requirements
Must have
• A green feeling that makes sure they understand that this product is a repellant and safe.
The Website must have the ability to grow outside the B-gone product line as new itmes are introduced such as Septic Bio products that break down waste and even make plants grow faster without chemicals.
Nice to have
• We already have a logo and trade mark for both KLV and B-gone which I will attach. The B-gone logo comes in different colours and animal images.
We were thinking of a name Fennel Wanderers as well but went with B-gone.
Should not have
• A green sell using the fonts etc included in the logos

```html
<!DOCTYPE html>
<html lang="en">
<head>
<meta charset="utf-8">
<title>KLV – Kindly Living Ventures</title>
<link rel="stylesheet" href="https://fonts.googleapis.com/css2?family=PT+Sans:ital,wght@0,400;0,700;1,700&family=Open+Sans:wght@300;400;700&family=Kaushan+Script&display=swap">
<style>
:root{
  --green:#6cb82c;
  --green-dark:#3f8a12;
  --yellow:#ffd200;
  --header-top:#2e2e2e;
  --header-bottom:#121212;
  --text:#ffffff;
  --muted:#cfcfcf;
  --footer:#1c1c1c;
  --rule:#7a7a7a;
}
*{margin:0;padding:0;box-sizing:border-box}
html,body{width:1100px;height:1200px;overflow:hidden;background:#111}
body{position:relative;font-family:"PT Sans",sans-serif;color:var(--text)}
.abs{position:absolute}

.site-header{left:0;top:0;width:1100px;height:128px;background:linear-gradient(var(--header-top),var(--header-bottom));border-bottom:2px solid #555}
.brand{left:80px;top:8px;width:255px;height:107px;display:flex;align-items:center;gap:14px}
.brand-dot{width:60px;height:60px;border-radius:50%;background:var(--green)}
.brand-name{font-family:"PT Sans",sans-serif;font-weight:700;font-size:62px;color:var(--green);line-height:1}
.phone{left:750px;top:13px;display:flex;align-items:center;gap:10px}
.phone-icon{width:37px;height:37px;border-radius:6px;background:#0c0c0c;display:flex;align-items:center;justify-content:center}
.phone-number{font-family:"Open Sans",sans-serif;font-weight:300;font-size:31px;color:#9a9a9a;letter-spacing:1px}
.main-nav{left:381px;top:86px;height:32px}
.main-nav a{position:absolute;top:0;height:32px;line-height:32px;font-family:"Open Sans",sans-serif;font-size:17px;color:#c8c8c8;text-decoration:none;white-space:nowrap}
.main-nav a.active{background:linear-gradient(#7fd13a,var(--green-dark));color:#fff;border-radius:3px 3px 0 0;width:95px;text-align:center}
.nav-sep{position:absolute;top:14px;height:26px;border-left:1px dotted #555}

.backdrop{left:0;top:130px;width:1100px;height:912px;background:linear-gradient(90deg,#4d6b1a 0%,#2c3d10 6%,#15200a 30%,#1a2a0c 50%,#15200a 70%,#2c3d10 94%,#5a7a22 100%)}
.content-panel{left:63px;top:130px;width:975px;height:912px;background:linear-gradient(rgba(10,14,6,.55),rgba(6,10,4,.75));border-left:1px solid #6a6a6a;border-right:1px solid #6a6a6a}

.hero{left:114px;top:143px;width:873px;height:370px;background:#fff;padding:6px}
.hero-photo{width:100%;height:100%;background:linear-gradient(90deg,#6f6a55 0%,#4a5a2a 25%,#3f8f1a 50%,#5f8a2c 75%,#8a7a5a 100%);position:relative}
.hero-badge{left:19px;top:12px;width:194px;height:116px;border:1px solid #ccc;padding:5px;background:transparent}
.hero-badge div{width:100%;height:100%;background:#fff;display:flex;align-items:center;justify-content:center;font-weight:700;font-size:36px;color:#222}
.hero-title{left:0;width:100%;top:182px;text-align:center;padding-left:140px;font-family:"Open Sans",sans-serif;font-weight:700;font-size:44px;color:#fff;letter-spacing:-.5px;text-shadow:0 2px 4px rgba(0,0,0,.6);line-height:1}
.hero-sub{left:252px;top:222px;font-family:"Open Sans",sans-serif;font-weight:400;font-size:47px;color:var(--yellow);letter-spacing:-1px;white-space:nowrap;line-height:1;text-shadow:0 2px 4px rgba(0,0,0,.5)}

.welcome-icon{left:83px;top:524px;width:45px;height:45px;border-radius:50%;background:radial-gradient(circle at 40% 35%,#9ee05a,var(--green-dark))}
.welcome-script{left:142px;top:528px;font-family:"Kaushan Script",cursive;font-size:34px;color:var(--green);line-height:1}
.welcome-title{left:84px;top:572px;font-family:"Open Sans",sans-serif;font-size:22px;letter-spacing:4.3px;color:#fff;line-height:1}
.welcome-rule{left:84px;top:606px;width:932px;border-top:1px dotted #777}
.welcome-copy{left:84px;top:614px;width:930px;font-size:12px;line-height:20px}

.col-rule{top:745px;height:292px;border-left:1px dotted #666}
.section-icon{border-radius:50%}
.section-title{font-family:"Open Sans",sans-serif;font-size:22px;color:#fff;line-height:1;white-space:nowrap}
.section-title span{color:var(--green)}
.col-copy{font-size:12px;line-height:20px;text-align:justify}

.product-card{left:91px;top:786px;width:252px;height:136px;background:#fff;display:flex;align-items:center;justify-content:center;font-weight:700;font-size:44px;color:#222}
.quality-art{left:405px;top:780px;width:267px;height:122px;background:linear-gradient(160deg,#e8e0dc,#c21e1e 40%,#b01818 60%,#e8e0dc);transform:rotate(-8deg);border-radius:4px}
.contact-art{left:710px;top:698px;width:80px;height:78px;border-radius:8px;background:linear-gradient(135deg,#e6e6e6,#8a8a8a 60%,var(--green))}
.contact-sub{left:708px;top:788px;font-style:italic;font-weight:700;font-size:18px;white-space:nowrap}
.contact-info{left:718px;top:836px;font-size:12px;line-height:20px}
.contact-info .pair{display:flex}
.contact-info .pair span{width:131px}

.site-footer{left:0;top:1042px;width:1100px;height:158px;background:linear-gradient(#1a1a1a,#262626);border-top:4px solid var(--rule)}
.footer-nav{left:0;top:1094px;width:1100px;font-family:"Open Sans",sans-serif;font-size:12px;color:#bbb;letter-spacing:.8px}
.footer-nav span{position:absolute;white-space:nowrap}
.copyright{left:0;top:1125px;width:1100px;text-align:center;font-family:"Open Sans",sans-serif;font-size:11px;color:#bbb;letter-spacing:.3px}
</style>
</head>
<body>

<header class="site-header abs">
  <div class="brand abs">
    <div class="brand-dot"></div>
    <div class="brand-name">KLV</div>
  </div>
  <div class="phone abs">
    <div class="phone-icon">
      <svg width="20" height="22" viewBox="0 0 20 22"><path d="M6 2c-2 1-4 3-3 7 1 5 5 10 9 11 3 1 5-1 6-2l-3-4-3 2c-2-1-4-4-5-7l3-2z" fill="#fff"/></svg>
    </div>
    <div class="phone-number">(123) 555 0188</div>
  </div>
  <nav class="main-nav abs">
    <a class="active" style="left:0">Home</a>
    <span class="nav-sep" style="left:98px"></span>
    <a style="left:118px">About Us</a>
    <span class="nav-sep" style="left:209px"></span>
    <a style="left:232px">Products</a>
    <span class="nav-sep" style="left:323px"></span>
    <a style="left:348px">Quality</a>
    <span class="nav-sep" style="left:425px"></span>
    <a style="left:450px">Enquiry</a>
    <span class="nav-sep" style="left:536px"></span>
    <a style="left:561px">Contact</a>
  </nav>
</header>

<div class="backdrop abs" role="img" aria-label="Bamboo forest background"></div>
<main class="content-panel abs"></main>

<section class="hero abs">
  <div class="hero-photo" role="img" aria-label="Raccoons, a green python and grazing kangaroos">
    <div class="hero-badge abs"><div>B-gone</div></div>
    <div class="hero-title abs">A NATURAL PRODUCT</div>
    <div class="hero-sub abs">Designed to Repel Animals</div>
  </div>
</section>

<div class="welcome-icon abs"></div>
<div class="welcome-script abs">Welcome to the</div>
<h1 class="welcome-title abs">Kindly Living Ventures</h1>
<div class="welcome-rule abs"></div>
<p class="welcome-copy abs">Lorem ipsum dolor sit amet, consectetur adipiscing elit. Sed at ante. Mauris eleifend, quam a vulputate dictum, massa quam dapibus leo, eget vulputate orci purus ut lorem. In fringilla mi in ligula. Pellentesque aliquam quam vel dolor. Nunc adipiscing. Sed quam odio, tempus ac, aliquam molestie, varius ac, tellus. Vestibulum ut nulla aliquam risus rutrum interdum. Pellentesque lorem. Curabitur sit amet erat quis risus feugiat viverra. Pellentesque augue justo, sagittis et, lacinia at, venenatis non, arcu. Nunc nec libero. In cursus dictum risus...</p>

<!-- Products -->
<div class="section-icon abs" style="left:85px;top:720px;width:55px;height:55px;background:radial-gradient(circle at 40% 35%,#9ee05a,#2f6a0c 70%,#222);border:3px solid #ddd"></div>
<h2 class="section-title abs" style="left:147px;top:733px"><span>Our</span> Products</h2>
<div class="product-card abs">B-gone</div>
<p class="col-copy abs" style="left:92px;top:937px;width:254px">Lorem ipsum dolor sit amet, consectetur adipiscing elit. Sed at ante. Mauris eleifend, quam a vulputate dictum, massa quam dapibus leo, eget vulputate orci purus ut lorem....</p>

<div class="col-rule abs" style="left:392px"></div>

<!-- Quality -->
<svg class="abs" style="left:401px;top:717px" width="58" height="58" viewBox="0 0 58 58">
  <circle cx="29" cy="29" r="28" fill="#f2b01e"/>
  <circle cx="29" cy="29" r="20" fill="#f7c845"/>
  <path d="M19 29l7 7 13-14" stroke="#fff" stroke-width="5" fill="none" stroke-linecap="round" stroke-linejoin="round"/>
</svg>
<h2 class="section-title abs" style="left:470px;top:733px"><span>Quality</span> Policy</h2>
<div class="quality-art abs" role="img" aria-label="Red quality stamp"></div>
<p class="col-copy abs" style="left:405px;top:920px;width:254px">Lorem ipsum dolor sit amet, consectetur adipiscing elit. Sed at ante. Mauris eleifend, quam a vulputate dictum, massa quam dapibus leo, eget vulputate orci purus ut lorem. Mauris eleifend, quam a vulputate dictum, ....</p>

<div class="col-rule abs" style="left:692px"></div>

<!-- Contact -->
<div class="contact-art abs" role="img" aria-label="Support agent with headset at a laptop"></div>
<h2 class="section-title abs" style="left:801px;top:727px"><span>Contact</span> Details</h2>
<div class="contact-sub abs">Kindly Living Ventures</div>
<address class="contact-info abs" style="font-style:normal">
  HEAD OFFICE<br>
  Lorem ipsum dolor sit amet,<br>
  Sydney, Australia<br>
  Tel:&nbsp; (123) 555 0188, Email: info@klv.com<br>
  <br>
  BRANCH OFFICE<br>
  <div class="pair"><span>Taiwan Office</span><span>China Office</span></div>
  <div class="pair"><span>Tel. (123) 555 0175</span><span>Tel. (123) 555 0175</span></div>
</address>

<footer class="site-footer abs"></footer>
<nav class="footer-nav abs">
  <span style="left:319px">Home</span>
  <span style="left:370px">|</span>
  <span style="left:393px">About Us</span>
  <span style="left:459px">|</span>
  <span style="left:479px">Products</span>
  <span style="left:550px">|</span>
  <span style="left:570px">Quality</span>
  <span style="left:625px">|</span>
  <span style="left:648px">Enquiry</span>
  <span style="left:715px">|</span>
  <span style="left:731px">Contact</span>
</nav>
<div class="copyright abs">Copyright © KLV.com, 2011-12. Terms &amp; Conditions &nbsp;| Privacy Policy</div>

</body>
</html>
```